Web Design - Fitness for Middle Age Women

I need a web design for a start-up personal training company in Los Alamitos, CA called 'Maple Fitness & Health.' I would like to cater personal training services to middle-age mothers (30-50 years of age) who have kids and who would also want their children to receive services. The attached file is the logo of the company. Keep in mind the theme colors are white and blue and black, but make the background/pictures appealing to middle-age mothers. I want the flow of the website to be easy to use. The final design should present the company as a professional personal training service.

I realize this is a low budget project for designers but this is a budget I have to offer at the moment and if I take your design I will make sure to come back to improve the site when I'm able to gain more capital. I am looking for a full website built (using wordpress) with the following tabs (About / FAQ / Services / Clients / Location / Contact Us...and social media links to Twitter / Instagram / Facebook)
Updates

I am looking over the current designs and narrowing down the decision. A decision will be made in the next 24-48 hours.

Target Market(s)

Middle-age mothers (30-55 years of age) who have children, an established career (or husband who is the bread-winner of the house) and has forgotten to take care of themselves and their body for years. I want them to realize lifestyle change is a choice, and it is a choice they need to make for themselves and their family to be a proper pattern for their children.

Industry/Entity Type

Fitness

Requirements
Must have
• The logo I have attached.

```html
<!DOCTYPE html>
<html lang="en">
<head>
<meta charset="utf-8">
<title>Maple Fitness &amp; Health</title>
<link href="https://fonts.googleapis.com/css2?family=Roboto:wght@300;400;500&display=swap" rel="stylesheet">
<style>
:root{
  --canvas:#ededed;
  --white:#ffffff;
  --ink:#222428;
  --navy:#1e2a5a;
  --blue:#2a62c9;
  --band-blue:#3a82f5;
  --card-blue:#1a4fa8;
  --pink:#f0196e;
  --green:#3cbf8e;
  --red:#e0141e;
  --grey:#8a8a8a;
  --nav-grey:#7a7a7a;
  --soft:#f6f6f6;
  --footer:#4f5358;
  --footer-bar:#3e4146;
  --footer-text:#d6d8db;
}
*{margin:0;padding:0;box-sizing:border-box}
html,body{width:1200px;height:1000px;overflow:hidden;background:var(--canvas);font-family:'Roboto',sans-serif;color:var(--ink)}
.site{position:absolute;left:352px;top:40px;width:496px;height:880px}
.abs{position:absolute}

/* header */
.brand{left:2px;top:5px;display:flex;align-items:center;gap:7px}
.brand-mark{width:36px;height:36px;border-radius:50%;background:var(--navy)}
.brand-name{font-size:10px;line-height:12px;color:var(--navy);font-weight:400}
.call{right:0;top:4px;text-align:right;color:var(--grey);font-size:8px;line-height:11px;font-weight:300}
.call .phone{font-size:14px;line-height:17px;color:var(--blue);font-weight:400}
.call .sub{font-size:9px}
.nav{right:3px;top:72px;display:flex;gap:6px;font-size:13px;color:var(--nav-grey);white-space:nowrap}
.nav .sep{color:#999}
.nav .current{color:var(--blue);font-weight:500}

/* hero */
.hero{left:0;top:111px;width:496px;height:236px;background:var(--white)}
.hero-photo{left:0;top:0;width:257px;height:236px;background:linear-gradient(135deg,#2d8ae8,#0f5cc4)}
.hero-copy{left:272px;top:62px;white-space:nowrap}
.hero-title{font-size:25px;line-height:31px;font-weight:300;color:var(--blue)}
.hero-sub{font-size:9px;margin-top:8px;color:#444}
.btn{display:inline-block;color:var(--white);font-size:11px;text-align:center;white-space:nowrap}
.btn-pink{left:317px;top:167px;width:127px;height:22px;line-height:22px;background:var(--pink)}

/* updates */
.updates{left:0;top:347px;width:344px;height:151px;background:var(--soft)}
.updates-title{left:33px;top:19px;font-size:14px;font-weight:400;display:flex;align-items:center;gap:8px}
.badge-new{background:var(--red);color:var(--white);font-size:6px;padding:2px 5px;font-weight:500}
.post{top:55px;width:120px}
.post-title{font-size:9px;color:var(--blue);white-space:nowrap}
.post-meta{font-size:6px;color:#555;margin-top:4px}
.post-body{font-size:6px;line-height:10px;color:#555;margin-top:10px}
.trial{left:344px;top:347px;width:152px;height:151px;background:linear-gradient(160deg,#1e5ec2,var(--card-blue))}
.trial-num{left:25px;top:6px;font-size:44px;font-weight:300;color:var(--white);line-height:44px}
.trial-head{left:62px;top:12px;font-size:13px;line-height:18px;color:var(--white);white-space:nowrap}
.trial-sub{left:62px;top:49px;font-size:8px;color:#dfe8ff;white-space:nowrap}
.btn-green{left:29px;top:101px;width:94px;height:23px;line-height:23px;background:var(--green)}

/* classes */
.classes{left:0;top:498px;width:496px;height:219px;background:var(--band-blue);color:var(--white)}
.classes-title{left:0;top:20px;width:100%;text-align:center;font-size:14px;font-weight:300}
.class{top:71px;width:110px;text-align:center}
.class-photo{width:82px;height:82px;border-radius:50%;border:2px solid var(--white);margin:0 auto;background:linear-gradient(135deg,#cfd8e8,#8aa3c9)}
.class-name{font-size:9px;margin-top:14px}
.class-text{font-size:6.5px;line-height:9px;margin-top:8px}

/* footer */
.footer{left:0;top:717px;width:496px;height:133px;background:var(--footer);color:var(--footer-text)}
.col-head{font-size:9px;top:22px}
.col-text{font-size:6px;line-height:8px;top:51px}
.divider{top:21px;height:88px;border-left:1px dotted #9a9ea3}
.social{width:22px;height:22px;border-radius:50%}
.footer-bar{left:0;top:850px;width:496px;height:30px;background:var(--footer-bar);color:#a9acb0;font-size:7px;text-align:center;line-height:30px}
.shadow{left:0;width:496px;box-shadow:0 6px 14px rgba(0,0,0,.18)}
</style>
</head>
<body>
<div class="site">
  <div class="abs shadow" style="top:111px;height:769px"></div>

  <header>
    <div class="abs brand"><span class="brand-mark"></span><span class="brand-name">Maple<br>Fitness &amp; Health</span></div>
    <div class="abs call">CALL US TODAY ON<div class="phone">1-555-0140</div><div class="sub">to start getting fit!</div></div>
    <nav class="abs nav"><span class="current">About</span><span class="sep">/</span><span>FAQ</span><span class="sep">/</span><span>Services</span><span class="sep">/</span><span>Clients</span><span class="sep">/</span><span>Location</span><span class="sep">/</span><span>Contact Us</span></nav>
  </header>

  <section class="abs hero">
    <div class="abs hero-photo" role="img" aria-label="Photo of a cheering woman with a towel around her neck on a blue backdrop"></div>
    <div class="abs hero-copy">
      <h1 class="hero-title" style="font-weight:300">READY TO STEP UP<br>YOUR TRAINING</h1>
      <p class="hero-sub">start maximizing your workout toay!</p>
    </div>
    <span class="abs btn btn-pink">WORK IT OUT NOW !</span>
  </section>

  <section class="abs updates">
    <h2 class="abs updates-title">RECENT UPDATE <span class="badge-new">NEW</span></h2>
    <article class="abs post" style="left:33px">
      <div class="post-title">Yoga Classs cancel on 25.12.14</div>
      <div class="post-meta"><i>admin post on 10.12.2014</i></div>
      <p class="post-body">Lorem ipsum dolor sit amet, consectetuer adipiscing elit. Aenean commodo ligula eget dolor. Aenean massa. Cum sociis natoque penatibus et magnis dis parturient montes,</p>
    </article>
    <article class="abs post" style="left:195px">
      <div class="post-title">24 hours on New Year Eve!</div>
      <div class="post-meta"><i>admin post on 10.12.2014</i></div>
      <p class="post-body">Lorem ipsum dolor sit amet, consectetuer adipiscing elit. Aenean commodo ligula eget dolor. Aenean massa. Cum sociis natoque penatibus et magnis dis parturi-</p>
    </article>
  </section>

  <aside class="abs trial" role="img" aria-label="Faded photo of a woman exercising behind the free trial offer">
    <div class="abs trial-num">7</div>
    <div class="abs trial-head">Days<br>Free Trial</div>
    <div class="abs trial-sub">it's time to get fit!</div>
    <span class="abs btn btn-green">TRY NOW !!</span>
  </aside>

  <section class="abs classes">
    <h2 class="abs classes-title" style="font-weight:300">CHOOSE CLASSES FOR YOUR SPORT LIFE</h2>
    <div class="abs class" style="left:13px"><div class="class-photo" role="img" aria-label="Photo of a step aerobics group class"></div><div class="class-name">BODY STEP</div><p class="class-text">Lorem ipsum dolor sit amet, con-<br>sectetuer adipiscing elit. Aenean</p></div>
    <div class="abs class" style="left:132px"><div class="class-photo" role="img" aria-label="Photo of women stretching in a yoga pilates class"></div><div class="class-name">YOGA PILATES</div><p class="class-text">Lorem ipsum dolor sit amet, con-<br>sectetuer adipiscing elit. Aenean</p></div>
    <div class="abs class" style="left:251px"><div class="class-photo" role="img" aria-label="Photo of a woman on an exercise bike"></div><div class="class-name">CARDIO FITNESS</div><p class="class-text">Lorem ipsum dolor sit amet, con-<br>sectetuer adipiscing elit. Aenean</p></div>
    <div class="abs class" style="left:368px"><div class="class-photo" role="img" aria-label="Photo of a boxing training session"></div><div class="class-name">BOXING</div><p class="class-text">Lorem ipsum dolor sit amet, con-<br>sectetuer adipiscing elit. Aenean</p></div>
  </section>

  <footer class="abs footer">
    <div class="abs col-head" style="left:45px">Opening Hours</div>
    <div class="abs col-text" style="left:45px">Monday to Friday<br>07:00 - 12:00<br><br>Saturday to Sunday<br>08:00 - 11:00</div>
    <div class="abs divider" style="left:152px"></div>
    <div class="abs col-head" style="left:199px">Contact Us</div>
    <div class="abs col-text" style="left:199px">Any question ? Email us!<br>info@maplefitness.com<br><br>Give us a call<br>1-555-01400</div>
    <div class="abs divider" style="left:326px"></div>
    <div class="abs col-head" style="left:374px">Follow Us</div>
    <span class="abs social" style="left:378px;top:51px;background:#e0141e" aria-label="Video channel"></span>
    <span class="abs social" style="left:412px;top:51px;background:#2fa6e0" aria-label="Microblog"></span>
    <span class="abs social" style="left:378px;top:83px;background:#2c2d30" aria-label="Social network"></span>
    <span class="abs social" style="left:412px;top:83px;background:#2d5ba8" aria-label="Community page"></span>
  </footer>
  <div class="abs footer-bar">© 2012-2015 MAPLE FITNESS &amp; Health. All Rights Reserved.</div>
</div>
</body>
</html>
```